Saffron Hearth Roti/Naan bread packaging for Australia

We would like to update and refresh the packaging design for our Saffron Hearth bread range. These breads are currently being sold in Australian supermarkets and are very popular. The proposed design should have some "continuity" with the current packaging design so that consumers can still recognise the brand/product easily on shelf. The design should suggest "fresh, tasty, healthy, authentic and Australian-made".
FYI, the products are not chilled or frozen - they sit on the regular supermarket shelves and will need to stand out. The breads will typically sit next to each other on the shelf, but usually just one facing each. I'll be uploading image files of the current packaging for your reference.
Updates

Hi all, I just uploaded the current logo for those of you who want it.  Also, there are printer details in the discussion area that you might find useful.  I am hoping to get their design template in the next day or so, but don't let that stop you from starting.  We are only looking for a design concept that we can use across the product range.  Cheers!

Hi, I've uploaded the design template/layers for those who would like this.  Cheers!

Hi everyone, thanks to those of you who have either submitted or are working on designs.  I have reviewed the available designs with the MD and will be providing individual feedback to you wherever possible.

Lastly, we'll be extending the deadline for a few more days to allow for changes and resubmissions.

Good luck everyone!

Reason: To allow for changes and resubmissions - will be providing individual feedback to all designs submitted. Cheers.

Reason: One last extension before we award the guaranteed prize.

Target Market(s)

Australian consumers who eat Indian foods and would pay a premium for a better product

Industry/Entity Type

Product

Requirements
Must have
• Transparent window to show breads
Some carryover elements from current packaging for consumer recognition
Same product info on the back (i.e. Nutritional Info panel, Heating Instructions, Barcode, Company details, Usage Suggestions)
Nice to have
• The design should suggest "fresh, tasty, healthy, authentic and Australian-made".

```html
<!DOCTYPE html>
<html lang="en">
<head>
<meta charset="utf-8">
<title>Saffron Hearth Roti Bread – Pack Front</title>
<link rel="stylesheet" href="https://fonts.googleapis.com/css2?family=Rozha+One&family=Fredoka:wght@600&family=Delius&family=Kalam:wght@400&display=swap">
<style>
  :root {
    --saffron: #ffb21c;
    --orange: #ff6a1a;
    --red: #d01212;
    --deep-red: #c00a0a;
    --wheat-red: #e31b1b;
    --gold: #ffe23a;
    --ornament: #ffd27a;
    --ink: #111111;
    --banner-text: #c8101a;
    --white: #ffffff;
    --veg-green: #2fd12f;
  }
  * { margin: 0; padding: 0; box-sizing: border-box; }
  html, body { width: 951px; height: 1200px; overflow: hidden; background: var(--white); }
  .pack {
    position: relative;
    width: 951px;
    height: 1200px;
    overflow: hidden;
    background: linear-gradient(to bottom,
      var(--saffron) 0px, var(--saffron) 149px,
      #ffa41c 180px, var(--orange) 330px, #e9311a 430px, var(--red) 540px, var(--red) 1115px);
  }
  .top-band {
    position: absolute; left: 0; top: 0; width: 951px; height: 149px;
    background: var(--saffron);
  }
  .handle-slot {
    position: absolute; left: 372px; top: 65px; width: 206px; height: 40px;
    background: var(--white); border-radius: 20px; border: 1px solid #d9a03a;
  }
  .wheat-field {
    position: absolute; left: 0; top: 818px; width: 951px; height: 297px;
    background: linear-gradient(to bottom, rgba(227,27,27,0) 0%, rgba(227,27,27,0.55) 35%, var(--wheat-red) 100%);
  }
  .bottom-band {
    position: absolute; left: 0; top: 1115px; width: 951px; height: 85px;
    background: var(--deep-red);
  }
  .ornament {
    position: absolute; top: 212px; width: 168px; height: 100px;
    background: radial-gradient(ellipse at center, rgba(255,210,122,0.55) 0%, rgba(255,210,122,0.15) 70%, rgba(255,210,122,0) 100%);
    border-radius: 50%;
  }
  .ornament--left { left: 131px; }
  .ornament--right { left: 651px; }
  .brand-name {
    position: absolute; left: 0; top: 200px; width: 951px;
    text-align: center;
    font-family: "Rozha One", serif;
    font-size: 60px; line-height: 1;
    color: var(--gold);
  }
  .brand-rule {
    position: absolute; left: 322px; top: 318px; width: 307px; height: 0;
    border-top: 2px dotted var(--ornament);
  }
  .product-name {
    position: absolute; left: 0; top: 334px; width: 951px;
    text-align: center;
    font-family: "Fredoka", sans-serif; font-weight: 600;
    font-size: 50px; line-height: 1.1;
    color: #fff07a;
    -webkit-text-stroke: 2px #3a1a00;
    paint-order: stroke fill;
  }
  .origin {
    position: absolute; left: 0; top: 400px; width: 951px;
    text-align: center;
    font-family: "Delius", sans-serif;
    font-size: 24px; color: var(--ink);
  }
  .window {
    position: absolute; left: 212px; top: 456px; width: 526px; height: 326px;
  }
  .flavour {
    position: absolute; left: 0; top: 788px; width: 951px;
    text-align: center;
    font-family: "Kalam", cursive;
    font-size: 33px; color: var(--ink); line-height: 1.2;
  }
  .banner {
    position: absolute;
  }
  .banner--tasty { left: 358px; top: 843px; width: 238px; height: 58px; }
  .banner--fresh { left: 375px; top: 914px; width: 206px; height: 52px; }
  .banner-label {
    position: absolute; inset: 0;
    display: flex; align-items: center; justify-content: center;
    font-family: "Kalam", cursive;
    color: var(--banner-text);
  }
  .banner--tasty .banner-label { font-size: 26px; }
  .banner--fresh .banner-label { font-size: 23px; }
  .net-weight {
    position: absolute; left: 41px; top: 1057px;
    display: flex; align-items: center; gap: 12px;
    font-family: Arial, Helvetica, sans-serif;
    font-size: 17px; color: var(--ink);
  }
  .veg-mark {
    width: 21px; height: 21px; background: var(--white);
    border: 2px solid var(--veg-green);
    display: flex; align-items: center; justify-content: center;
  }
  .veg-mark span { width: 11px; height: 11px; border-radius: 50%; background: var(--veg-green); }
  .cert-badge {
    position: absolute; left: 838px; top: 1020px; width: 82px; height: 82px;
    border-radius: 50%; border: 2px solid #f3d9d9;
  }
</style>
</head>
<body>
  <main class="pack">
    <div class="top-band"><div class="handle-slot"></div></div>

    <div class="wheat-field" role="img" aria-label="Red wheat stalk silhouettes across the lower pack"></div>
    <div class="bottom-band"></div>

    <div class="ornament ornament--left" role="img" aria-label="Gold filigree ornament"></div>
    <div class="ornament ornament--right" role="img" aria-label="Gold filigree ornament"></div>
    <h1 class="brand-name">Saffron Hearth</h1>
    <div class="brand-rule"></div>

    <h2 class="product-name">Roti Bread</h2>
    <p class="origin">Australian Made</p>

    <svg class="window" viewBox="0 0 526 326" aria-label="Transparent window showing the breads">
      <rect x="6" y="6" width="514" height="314" fill="#ffffff" stroke="#f7a72a" stroke-width="8" stroke-dasharray="6 6"/>
      <rect x="10" y="10" width="506" height="306" fill="#ffffff"/>
    </svg>

    <p class="flavour">Garlic Flavour</p>

    <div class="banner banner--tasty">
      <svg width="238" height="58" viewBox="0 0 238 58">
        <path d="M4 6 Q60 0 119 6 T234 4 L226 29 L234 54 Q178 48 119 54 T4 52 L12 29 Z" fill="#ffffff"/>
      </svg>
      <span class="banner-label">Tasty &amp; Healthy</span>
    </div>
    <div class="banner banner--fresh">
      <svg width="206" height="52" viewBox="0 0 206 52">
        <path d="M4 6 Q52 0 103 6 T202 4 L195 26 L202 48 Q154 42 103 48 T4 46 L11 26 Z" fill="#ffffff"/>
      </svg>
      <span class="banner-label">Fresh &amp; Pure</span>
    </div>

    <div class="net-weight">
      <div class="veg-mark"><span></span></div>
      <span>280 gm. NET</span>
    </div>

    <div class="cert-badge"></div>
  </main>
</body>
</html>
```